Franchise Vacation Rental Company Website

We are looking for fresh, new and creative design ideas to help enhance this site. We are a vacation rental company that is starting a new franchise business. This will be our home franchise page, and will need to appeal to franchise candidates as well as travelers looking for vacation homes in our current locations.

Business

```html
<!DOCTYPE html>
<html lang="en">
<head>
<meta charset="utf-8">
<title>BrightStays – Vacation Rental Services</title>
<link rel="stylesheet" href="https://fonts.googleapis.com/css2?family=Ubuntu:wght@300;400;500&family=Roboto+Condensed:wght@700&display=swap">
<style>
  :root {
    --green: #8dc63f;
    --green-dark: #6fa72a;
    --ink: #333333;
    --muted: #999999;
    --band: #2a3038;
    --band-edge: #1e2329;
    --footer: #1f1f1f;
    --footer-text: #8a8a8a;
    --white: #ffffff;
    --sky-top: #9fd2ef;
    --sky-bottom: #5fb2e4;
    --tile-label: #0d0d0d;
  }
  * { box-sizing: border-box; margin: 0; padding: 0; }
  html, body { width: 780px; height: 1200px; overflow: hidden; background: var(--white); }
  body { position: relative; font-family: "Ubuntu", sans-serif; color: var(--ink); }
  .abs { position: absolute; }

  /* header */
  .brand { left: 152px; top: 29px; font-size: 19px; font-weight: 400; color: var(--green); }
  .main-nav { left: 254px; top: 31px; display: flex; align-items: center; font-size: 8px; color: var(--muted); }
  .main-nav a { color: inherit; text-decoration: none; margin-right: 26px; }
  .main-nav .is-active { position: relative; background: var(--green); color: var(--white); padding: 4px 12px; margin-right: 24px; }
  .main-nav .is-active::after { content: ""; position: absolute; left: 50%; bottom: -4px; margin-left: -4px; border: 4px solid transparent; border-bottom: 0; border-top-color: var(--green); }

  /* hero */
  .hero-scene { left: 152px; top: 71px; width: 476px; height: 187px; background: linear-gradient(180deg, var(--sky-top), var(--sky-bottom)); }
  .hero-floor { left: 80px; top: 240px; width: 620px; height: 85px; background: radial-gradient(ellipse at 50% 30%, #e7ecef 0%, #f6f8f9 55%, rgba(255,255,255,0) 75%); }
  .hero-title { left: 192px; top: 132px; background: var(--green); color: var(--white); font-family: "Roboto Condensed", sans-serif; font-weight: 700; font-size: 34px; line-height: 33px; padding: 0 16px 0 3px; }
  .hero-subtitle { left: 194px; top: 166px; color: var(--white); font-size: 20px; font-weight: 300; }

  /* search band */
  .search-band { left: 27px; top: 354px; width: 726px; height: 377px; background: radial-gradient(ellipse at 50% 50%, #353c45 0%, var(--band) 60%, var(--band-edge) 100%); }
  .search-title { left: 173px; top: 417px; color: var(--white); font-size: 17px; font-weight: 400; }
  .search-field { left: 165px; width: 125px; height: 20px; border: 1px solid #5a6068; color: var(--white); font-size: 8px; padding: 5px 8px; }
  .search-field.destination { top: 447px; }
  .search-field.room { top: 471px; }
  .search-button { left: 165px; top: 496px; width: 125px; height: 20px; background: var(--green); color: var(--white); font-size: 8.5px; text-align: center; line-height: 20px; }

  .rental-tile { width: 152px; height: 125px; }
  .tile-photo { width: 100%; height: 100%; }
  .photo-harbour { background: linear-gradient(180deg, #6f9fd8 0%, #c8d8e6 45%, #4f6a4a 75%, #2d3b2e 100%); }
  .photo-marina { background: linear-gradient(180deg, #2c4f9a 0%, #6a86b8 40%, #d7dde3 65%, #2f3a52 100%); }
  .photo-island { background: linear-gradient(180deg, #f3f5f7 0%, #cfd6da 45%, #6c7d56 65%, #8a8e84 100%); }
  .tile-label { position: absolute; left: 8px; bottom: -14px; width: 137px; height: 28px; background: var(--tile-label); color: var(--white); font-size: 9px; text-align: center; line-height: 28px; }

  /* signup */
  .signup-panel { left: 151px; top: 713px; width: 474px; height: 53px; background: var(--white); box-shadow: 0 8px 8px -6px rgba(0,0,0,0.25); }
  .signup-text { left: 177px; top: 732px; font-size: 10px; color: #666; }
  .signup-input { left: 341px; top: 729px; width: 168px; height: 22px; border: 1px solid #e2e2e2; background: #f7f7f7; font-size: 7.5px; color: var(--muted); padding: 6px 10px; }
  .signup-submit { left: 519px; top: 729px; width: 81px; height: 22px; background: var(--green); color: var(--white); font-size: 8px; text-align: center; line-height: 22px; }

  /* features */
  .feature { width: 140px; text-align: center; top: 816px; }
  .feature-title { font-size: 10px; color: var(--ink); height: 26px; }
  .feature-icon { display: block; margin: 0 auto; }
  .feature-text { font-size: 6.5px; line-height: 8px; color: #444; margin-top: 16px; }

  /* footer */
  .site-footer { left: 27px; top: 1006px; width: 726px; height: 173px; background: var(--footer); }
  .footer-heading { top: 1033px; font-size: 11px; color: #b5b5b5; }
  .footer-links { left: 151px; top: 1057px; list-style: none; font-size: 8.5px; color: var(--footer-text); line-height: 14.5px; }
  .contact-line { left: 332px; font-size: 8.5px; color: var(--footer-text); display: flex; align-items: center; gap: 6px; }
  .social-list { left: 495px; top: 1060px; display: flex; gap: 4px; list-style: none; }
  .social-list li { width: 22px; height: 22px; background: #4a4a4a; }
  .social-list li:nth-child(odd) { background: #5a5a5a; }
</style>
</head>
<body>

<header>
  <div class="abs brand">BrightStays</div>
  <nav class="abs main-nav">
    <a class="is-active" href="#">Home</a>
    <a href="#">Spots</a>
    <a href="#">Franchise</a>
    <a href="#">List Properties</a>
    <a href="#">Rentals</a>
    <a href="#">News</a>
    <a href="#">Contact</a>
  </nav>
</header>

<section class="hero">
  <div class="abs hero-floor" role="img" aria-label="White wooden deck floor fading into the page"></div>
  <div class="abs hero-scene" role="img" aria-label="Seaside scene with a white sofa, potted plant, a businessman seated on a chair and a small wooden table"></div>
  <h1 class="abs hero-title">Vacation</h1>
  <div class="abs hero-subtitle">Rental Services</div>
</section>

<section class="search">
  <div class="abs search-band"></div>
  <h2 class="abs search-title">Search Rentals</h2>
  <div class="abs search-field destination">Destination</div>
  <div class="abs search-field room">Room</div>
  <div class="abs search-button">Search</div>

  <div class="abs rental-tile" style="left:312px;top:400px">
    <div class="tile-photo photo-marina" role="img" aria-label="Sailboats moored at a marina"></div>
    <div class="tile-label">Maryland Eastern Shore</div>
  </div>
  <div class="abs rental-tile" style="left:473px;top:400px">
    <div class="tile-photo photo-island" role="img" aria-label="Castle on a small island across a bay"></div>
    <div class="tile-label">Maryland Eastern Shore</div>
  </div>
  <div class="abs rental-tile" style="left:152px;top:550px">
    <div class="tile-photo photo-harbour" role="img" aria-label="Harbour with boats under a blue sky"></div>
    <div class="tile-label">Maryland Eastern Shore</div>
  </div>
  <div class="abs rental-tile" style="left:312px;top:550px">
    <div class="tile-photo photo-island" role="img" aria-label="Castle on a small island across a bay"></div>
    <div class="tile-label">Maryland Eastern Shore</div>
  </div>
  <div class="abs rental-tile" style="left:473px;top:550px">
    <div class="tile-photo photo-harbour" role="img" aria-label="Harbour with boats under a blue sky"></div>
    <div class="tile-label">Maryland Eastern Shore</div>
  </div>
</section>

<section class="signup">
  <div class="abs signup-panel"></div>
  <div class="abs signup-text">Signup for last getaway deals</div>
  <div class="abs signup-input">Enter Your email</div>
  <div class="abs signup-submit">Submit</div>
</section>

<section class="features">
  <div class="abs feature" style="left:157px">
    <h3 class="feature-title">Great Spot</h3>
    <svg class="feature-icon" width="60" height="80" viewBox="0 0 60 80">
      <circle cx="30" cy="28" r="28" fill="var(--green)"/>
      <path d="M30 19a7 7 0 0 0-7 7c0 5 7 12 7 12s7-7 7-12a7 7 0 0 0-7-7z" fill="#fff"/>
      <circle cx="30" cy="26" r="2.6" fill="var(--green)"/>
      <line x1="30" y1="56" x2="30" y2="75" stroke="#c79a3a" stroke-width="1"/>
      <path d="M28 73l2 4 2-4z" fill="#c79a3a"/>
    </svg>
    <p class="feature-text">Lorem ipsum dolor sit<br>amet this is a dummy texts lorem<br>ipsum dolor sit amet</p>
  </div>
  <div class="abs feature" style="left:312px">
    <h3 class="feature-title">Spot Travels free</h3>
    <svg class="feature-icon" width="60" height="80" viewBox="0 0 60 80">
      <circle cx="30" cy="28" r="28" fill="var(--green)"/>
      <ellipse cx="30" cy="30" rx="4" ry="8" fill="#fff"/>
      <circle cx="28" cy="19" r="1.8" fill="#fff"/>
      <circle cx="32" cy="18.5" r="1.5" fill="#fff"/>
      <circle cx="35" cy="20" r="1.3" fill="#fff"/>
      <line x1="30" y1="56" x2="30" y2="75" stroke="#c79a3a" stroke-width="1"/>
      <path d="M28 73l2 4 2-4z" fill="#c79a3a"/>
    </svg>
    <p class="feature-text">Lorem ipsum dolor sit<br>amet this is a dummy texts lorem<br>ipsum dolor sit amet</p>
  </div>
  <div class="abs feature" style="left:467px">
    <h3 class="feature-title">Last Min Deads</h3>
    <svg class="feature-icon" width="60" height="80" viewBox="0 0 60 80">
      <circle cx="30" cy="28" r="28" fill="var(--green)"/>
      <circle cx="30" cy="28" r="8.5" fill="none" stroke="#fff" stroke-width="1.6"/>
      <path d="M30 23v5h-4" fill="none" stroke="#fff" stroke-width="1.6"/>
      <line x1="30" y1="56" x2="30" y2="75" stroke="#c79a3a" stroke-width="1"/>
      <path d="M28 73l2 4 2-4z" fill="#c79a3a"/>
    </svg>
    <p class="feature-text">Lorem ipsum dolor sit<br>amet this is a dummy texts lorem<br>ipsum dolor sit amet</p>
  </div>
</section>

<footer>
  <div class="abs site-footer"></div>
  <h4 class="abs footer-heading" style="left:151px">Know More About US</h4>
  <ul class="abs footer-links">
    <li>Who we are?</li>
    <li>What we do?</li>
    <li>Franchise information</li>
    <li>Our Philosophy</li>
  </ul>

  <h4 class="abs footer-heading" style="left:332px">Contact Us</h4>
  <div class="abs contact-line" style="top:1058px">
    <svg width="10" height="10" viewBox="0 0 10 10"><path d="M2 0.5l2 2-1 1.2c.6 1.3 1.7 2.4 3 3l1.2-1 2 2-1.3 1.6C4.5 9 1 5.5.4 1.8z" fill="#9a9a9a"/></svg>
    <span>+1 555 014 2290</span>
  </div>
  <div class="abs contact-line" style="top:1078px">
    <svg width="10" height="8" viewBox="0 0 10 8"><rect width="10" height="8" fill="#9a9a9a"/><path d="M0 0l5 4 5-4" fill="none" stroke="#1f1f1f" stroke-width="1"/></svg>
    <span>hello@brightstays.example</span>
  </div>

  <h4 class="abs footer-heading" style="left:495px">Find us on</h4>
  <ul class="abs social-list" aria-label="Social links">
    <li></li><li></li><li></li><li></li><li></li>
  </ul>
</footer>

</body>
</html>
```